Bright Steps, Clear Minds - Poster

We currently have an updated flyer that was a set of a suite of materials. We would now like to update the posters to have a similar look and feel. There is a horizontal and a verticle (18 x 24 in) poster option.

I have attached 4 documents. 3 are the front page of the document featuring different people and 1 is the 2nd page of the document.

I also have attached the previously used poster. Please update the posters to match our newly updated materials. Please update the posters to match both visually and with the same text, funding, logo,etc.

```html
<!DOCTYPE html>
<html lang="en">
<head>
<meta charset="utf-8">
<title>Bright Steps, Clear Minds – Poster</title>
<link href="https://fonts.googleapis.com/css2?family=Montserrat:wght@700;800&family=Open+Sans:ital,wght@0,400;0,600;0,700;1,700&family=Arimo:ital,wght@0,400;0,700;1,400;1,700&display=swap" rel="stylesheet">
<style>
:root{
  --cream:#f8ece1;
  --cream-deep:#efe0d4;
  --brown:#4a2b25;
  --crimson:#9b1b30;
  --text:#3a3330;
  --footer:#cbbdb2;
  --rule:#b8283e;
}
*{box-sizing:border-box;margin:0;padding:0}
html,body{width:900px;height:1200px;overflow:hidden;background:var(--cream)}
.poster{position:relative;width:900px;height:1200px;overflow:hidden;
  background:linear-gradient(180deg,var(--cream) 0%,#fbf1e8 45%,var(--cream-deep) 100%);
  font-family:"Arimo",Arial,sans-serif;color:var(--text)}
.abs{position:absolute}
.portrait{left:500px;top:0;width:400px;height:610px;
  background:radial-gradient(ellipse 60% 55% at 62% 42%,#b89a86 0%,#c9ab98 35%,#d8bfb5 60%,rgba(248,236,225,0) 100%),
  radial-gradient(ellipse 55% 30% at 70% 92%,#c9a0c0 0%,rgba(248,236,225,0) 80%);}
.title{left:22px;top:14px;font-family:"Montserrat",sans-serif;font-weight:800;font-size:84px;line-height:63px;color:var(--brown);letter-spacing:-1px}
.subtitle{left:24px;top:168px;font-family:"Arimo",Arial,sans-serif;font-weight:700;font-size:21px;line-height:23px;color:var(--crimson)}
.intro{left:26px;top:220px;width:490px;font-size:9.8px;line-height:13.2px}
.stat-icon{background:var(--crimson)}
.map{left:43px;top:303px;width:96px;height:66px;border-radius:6px 14px 22px 10px}
.headdress{left:47px;top:484px;width:99px;height:117px;border-radius:50% 50% 40% 40%;background:linear-gradient(180deg,#8e2232,#5a2a28 70%,#c9b7a8)}
.stat{left:158px;font-family:"Open Sans",sans-serif;color:var(--crimson)}
.stat .num{font-size:37px;font-weight:700;letter-spacing:-1.5px;line-height:40px;display:inline-block;border-bottom:1.5px solid var(--crimson);padding-right:4px}
.stat .label{color:var(--brown);font-size:16.5px;line-height:16.5px;margin-top:6px}
.quote{left:600px;top:528px;width:232px;text-align:center;font-style:italic;font-size:13.2px;line-height:16.5px;color:var(--crimson)}
.quote b{font-weight:700}
.cta{left:40px;top:629px;width:412px;height:51px;border-radius:26px;background:var(--crimson);color:#fff;
  font-family:"Open Sans",sans-serif;font-style:italic;font-weight:700;font-size:15.2px;line-height:19px;text-align:center;padding-top:6px}
.col-head{top:699px;font-size:14.6px;font-weight:700;color:var(--crimson);text-align:center}
.doctor-list{left:45px;top:730px;width:400px;list-style:none;font-size:10.4px;line-height:13.2px}
.doctor-list li{position:relative;padding-left:20px}
.doctor-list li::before{content:"";position:absolute;left:1px;top:3px;width:7px;height:7px;background:var(--crimson);transform:rotate(45deg)}
.doctor-list b{color:var(--crimson)}
.doctor-list .sub{display:block;padding-left:25px}
.step{left:503px;width:340px;display:flex;gap:20px;font-size:10.4px;line-height:13.2px}
.step svg{flex:0 0 36px}
.step b{color:var(--crimson)}
.partners{left:0;top:1100px;width:900px;display:flex;justify-content:center;align-items:center;gap:34px;font-family:"Arimo",Arial,sans-serif;font-weight:700;font-size:12px;color:#4f9aa3}
.partner{display:flex;align-items:center;gap:7px}
.partner i{display:inline-block;width:34px;height:34px;border-radius:50%;background:#7fb6bb}
.partner.alt{color:var(--crimson)}
.footer{left:0;top:1156px;width:900px;height:44px;background:var(--footer);display:flex;align-items:center;padding:0 16px;gap:18px}
.footer .site{font-size:7px;font-weight:700;color:#4f9aa3;white-space:nowrap}
.footer p{font-size:5.6px;line-height:7.4px;color:#4d4541}
</style>
</head>
<body>
<div class="poster">
  <div class="abs portrait" role="img" aria-label="Portrait photograph of an elder woman with white hair over a soft woven-pattern backdrop"></div>

  <h1 class="abs title">Bright Steps,<br>Clear Minds…</h1>
  <h2 class="abs subtitle">The River of Life Flows Through the Heart,<br>Protecting the Mind and Body</h2>
  <p class="abs intro">Your heart health plays a big part in the health of your brain. Your heart is like the start of a flowing river. Blood vessels that take blood to and from your heart are like connected streams that flow through your body. They feed your brain with oxygen and energy.<br>You can do things to keep the streams freely flowing through your body, so your heart and brain stay strong and healthy.</p>

  <div class="abs stat-icon map" role="img" aria-label="Map of the United States"></div>
  <div class="abs stat" style="top:302px"><span class="num">5.7 Million</span><div class="label">Americans have<br>Alzheimer’s disease</div></div>

  <svg class="abs" style="left:57px;top:385px" width="80" height="96" viewBox="0 0 80 96" aria-label="Group of ten people, one highlighted">
    <defs>
      <g id="person" fill="none" stroke="var(--crimson)" stroke-width="1"><circle cx="0" cy="0" r="4"/><path d="M-4 6h8v12h-8z"/></g>
    </defs>
    <use href="#person" x="38" y="5"/><use href="#person" x="20" y="14"/><use href="#person" x="56" y="14"/>
    <use href="#person" x="6" y="36"/><use href="#person" x="70" y="36"/><use href="#person" x="10" y="60"/>
    <use href="#person" x="66" y="60"/><use href="#person" x="26" y="73"/><use href="#person" x="50" y="73"/>
    <g fill="var(--crimson)"><circle cx="38" cy="40" r="4"/><rect x="34" y="46" width="8" height="14"/></g>
  </svg>
  <div class="abs stat" style="top:392px"><span class="num">1 in 10</span><div class="label">People age 65 and older<br>has Alzheimer’s</div></div>

  <div class="abs headdress" role="img" aria-label="Illustration of a figure wearing a feathered headdress"></div>
  <div class="abs stat" style="top:478px"><span class="num">1 in 3</span><div class="label">American Indians over 65<br>develops dementia, including<br>Alzheimer’s</div></div>

  <p class="abs quote">Elders with <b>heart disease, high<br>blood pressure</b>, or <b>diabetes</b> have a<br>much higher risk of developing<br>Alzheimer's or other dementias.</p>

  <svg class="abs" style="left:0;top:590px" width="900" height="90" viewBox="0 0 900 90">
    <g fill="none" stroke="var(--rule)" stroke-width="1.3">
      <line x1="0" y1="64" x2="40" y2="64"/>
      <path d="M452 64H595l6-12 6 28 6-50 6 34h6c-6-8-8-16-2-20 6-4 12 0 14 6 2-6 8-10 14-6 6 4 4 12-2 20h6l6-18 5 30 5-44 6 32H900"/>
      <path d="M530 56c-6-12-2-28 12-32 14-4 28 4 28 18 0 10-6 14-6 22M530 56l-4 4 5 2 0 8h12" stroke-width="2"/>
      <path d="M538 36c4-4 10-4 14 0M536 44c6 2 12 0 18-2M544 30v14" stroke-width="1.5"/>
    </g>
  </svg>
  <div class="abs cta">Make an appointment with your doctor today to<br>talk about how to keep your mind and heart healthy.</div>

  <h3 class="abs col-head" style="left:60px;width:305px">Working with Your Doctor</h3>
  <ul class="abs doctor-list">
    <li><b>Make an appointment</b> for a “wellness” checkup with your doctor every year.
      <span class="sub">•You will get tests and screenings to make sure you are healthy.</span>
      <span class="sub">•They are usually free with Elder Care Plan B or the Tribal Care Program.</span>
      <span class="sub">•If you have concerns about your memory, talk to your doctor.</span></li>
    <li><b>Have your blood pressure checked</b> and know your numbers .
      <span class="sub">•Your blood pressure should be less than 120/80 mmHg (120 over 80)</span>
      <span class="sub">•If you do not know how to take your blood pressure, ask your doctor to</span>show you.</li>
    <li><b>Have your weight checked</b> regularly and know your number. If you need to lose extra weight, ask your doctor about:
      <span class="sub">•The right number of calories for your body</span>
      <span class="sub">•Ideas for healthier food choices</span>
      <span class="sub">•Support for losing weight</span></li>
    <li><b>If you smoke cigarettes or chew tobacco,</b> ask about medicine, counseling, or help to stop.</li>
    <li><b>If you do not have diabetes,</b> have your blood sugar level checked during your visit.<br>Your blood sugar should be less than 100 mg/dL when you have not eaten.</li>
    <li><b>If you do have diabetes,</b> go to regular doctor visits. Have your blood sugar and “A1C” levels checked. Your doctor will tell you what your A1C level should be.</li>
    <li><b>Talk with your doctor</b> about all the medicines and vitamins you take. Your doctor can make sure they do not cause any problems with your memory, sleep, or brain function.</li>
  </ul>

  <h3 class="abs col-head" style="left:560px;width:250px">Other Steps You Can Take</h3>

  <div class="abs step" style="top:726px"><svg width="36" height="36" viewBox="0 0 36 36"><g fill="none" stroke="var(--crimson)" stroke-width="1.3"><circle cx="18" cy="18" r="17"/><path d="M18 28C6 20 6 10 12 9c3 0 5 2 6 4 1-2 3-4 6-4 6 1 6 11-6 19zM5 19h8l2-4 3 8 2-4h11"/></g></svg><p><b>Aim for</b> 20 minutes of <b>physical activity</b> a day or 2 1/2 hours a week.</p></div>
  <div class="abs step" style="top:766px"><svg width="36" height="36" viewBox="0 0 36 36"><g fill="none" stroke="var(--crimson)" stroke-width="1.3"><circle cx="18" cy="18" r="17"/><path d="M7 14l22-6M7 18l22-6M14 26c0-4 3-6 4-6 1 0 4 2 4 6"/></g></svg><p><b>Read food labels</b> to see how much salt (sodium) or fat is in your food.</p></div>
  <div class="abs step" style="top:806px"><svg width="36" height="36" viewBox="0 0 36 36"><g fill="none" stroke="var(--crimson)" stroke-width="1.3"><circle cx="18" cy="18" r="17"/><path d="M13 10h5v6l3 4v9h-11v-9l3-4zM22 14h5l-2 8h-3M7 7l22 22"/></g></svg><p><b>Limit alcohol.</b> No more than 1 drink per day for women and 2 for men.</p></div>
  <div class="abs step" style="top:858px"><svg width="36" height="36" viewBox="0 0 36 36"><g fill="none" stroke="var(--crimson)" stroke-width="1.3"><path d="M18 2a16 15 0 1 1-9 27L4 33l2-7A16 15 0 0 1 18 2z"/><path d="M11 14h5l-5 6h5M18 10h5l-5 6h5M14 22h4l-4 5h4"/></g></svg><p><b>Get at least seven hours of sleep</b> each night. Talk to your doctor if you have trouble sleeping.</p></div>
  <div class="abs step" style="top:906px"><svg width="36" height="36" viewBox="0 0 36 36"><g fill="none" stroke="var(--crimson)" stroke-width="1.3"><circle cx="18" cy="18" r="17"/><path d="M11 8v8c0 2 3 2 3 0V8M12.5 16v13M18 8c-2 0-2 8 0 9v12M24 8v21M24 8c3 2 3 8 0 10"/></g></svg><p><b>Eat less</b> salt, sugar, red meat, and highly processed or packaged foods.</p></div>
  <div class="abs step" style="top:946px"><svg width="36" height="36" viewBox="0 0 36 36"><g fill="none" stroke="var(--crimson)" stroke-width="1.3"><rect x="2" y="2" width="32" height="32" rx="6"/><path d="M9 14a9 9 0 0 1 18 0zM18 14l3-4"/></g></svg><p><b>Manage extra weight</b> by making small changes. Losing a few pounds makes a difference.</p></div>
  <div class="abs step" style="top:998px"><svg width="36" height="36" viewBox="0 0 36 36"><g fill="none" stroke="var(--crimson)" stroke-width="1.3"><circle cx="18" cy="18" r="17"/><path d="M11 7v8a6 6 0 0 0 12 0V7M17 21v5a4 4 0 0 0 8 0v-3"/><circle cx="25" cy="21" r="2"/></g></svg><p><b>Take your medicine</b> for blood pressure, diabetes, and other problems even if you feel good.</p></div>
  <div class="abs step" style="top:1038px"><svg width="36" height="36" viewBox="0 0 36 36"><g fill="none" stroke="var(--crimson)" stroke-width="1.3"><path d="M10 34v-6c-4-3-6-8-5-13 2-8 10-12 18-10 8 3 10 11 7 17l-2 3v9"/><circle cx="18" cy="15" r="4"/><circle cx="18" cy="15" r="6.5" stroke-dasharray="2 2"/></g></svg><p><b>Keep your mind active.</b> Visit with people in your community, help plan tribal events, go to your senior center, teach your language, play cards, or start a new hobby.</p></div>

  <div class="abs partners">
    <span class="partner"><i></i>Northwind Center for Brain Health</span>
    <span class="partner alt">Keystone Health</span>
    <span class="partner" style="color:#3f9a4a">Cedar Aging Alliance</span>
    <span class="partner" style="color:#2b4f9c">National Health Agency</span>
  </div>

  <div class="abs footer">
    <span class="site">www.cedaraging.org</span>
    <p>This publication was supported by grant number 4NW22TC000487-02-01, funded by the National Health Agency (NHA). Its contents are solely the responsibility of the authors and do not necessarily represent the official views of the NHA or the Department of Public Wellness (DPW). The mark "NHA" is owned by DPW and is used with permission. Use of this logo is not an endorsement by DPW or NHA of any particular product, service, or enterprise.</p>
  </div>
</div>
</body>
</html>
```